Redesign my business cards

I would like pretty much all the same information as my current business cards but redesigned to stand out more and be more unique photo uploaded to show my current business cards don’t mind if you want to remove or replace I for on the back

```html
<!DOCTYPE html>
<html lang="en">
<head>
<meta charset="utf-8">
<title>Brightlane Detailing – Business Cards</title>
<link href="https://fonts.googleapis.com/css2?family=Exo+2:ital,wght@0,800;1,700;1,800&family=Manrope:wght@600;700;800&display=swap" rel="stylesheet">
<style>
:root{
  --navy:#023d55;
  --sky:#3cb4e5;
  --white:#ffffff;
  --ink:#000000;
  --silver:#d9dde0;
}
*{margin:0;padding:0;box-sizing:border-box}
html,body{width:1200px;height:3297px;overflow:hidden;background:var(--white)}
body{position:relative;font-family:"Manrope",sans-serif;color:var(--white)}
.card{position:absolute;left:86px;width:1028px;height:588px;background:var(--navy)}
.card--front{top:160px}
.card--back{top:906px}
.side-label{position:absolute;left:0;width:1200px;text-align:center;font-family:"Manrope",sans-serif;font-weight:800;font-size:40px;color:var(--ink)}
.banner{position:absolute;left:0;width:1200px;background:var(--navy)}
.brand{position:absolute;display:flex;align-items:center;gap:18px}
.brand__dot{border-radius:50%;flex:none}
.brand__name{font-family:"Exo 2",sans-serif;font-weight:800;line-height:0.95;letter-spacing:1px;text-transform:uppercase}
.brand--sky .brand__dot{background:var(--sky)} .brand--sky .brand__name{color:var(--sky)}
.brand--white .brand__dot{background:var(--white)} .brand--white .brand__name{color:var(--white)}
.brand--navy .brand__dot{background:var(--navy)} .brand--navy .brand__name{color:var(--navy)}
.brand--silver .brand__dot{background:var(--silver)} .brand--silver .brand__name{color:var(--silver)}
.contact{position:absolute;top:670px;left:318px;display:flex;align-items:center;gap:40px;font-weight:700;font-size:17px}
.contact__item{display:flex;align-items:center;gap:6px}
.contact__email{font-size:15px}
.service{position:absolute}
.service__title{display:flex;align-items:center;gap:16px;font-family:"Exo 2",sans-serif;font-style:italic;font-weight:700;font-size:30px;color:var(--sky);line-height:38px;margin-bottom:4px}
.price{background:var(--white);color:var(--navy);font-family:"Exo 2",sans-serif;font-style:italic;font-weight:800;font-size:21px;line-height:26px;padding:0 10px;transform:skewX(-10deg)}
.service__list{list-style:none}
.service__list li{position:relative;padding-left:29px;font-weight:700;font-size:21.5px;line-height:25.5px;margin-bottom:16px}
.service__list li::before{content:"";position:absolute;left:0;top:8px;width:15px;height:15px;border-radius:50%;background:var(--white)}
.owner{position:absolute;right:86px;top:222px;text-align:right}
.owner__name{font-weight:800;font-size:28px;line-height:32px}
.owner__role{font-weight:700;font-size:13px;letter-spacing:.5px}
</style>
</head>
<body>

<section class="card card--front">
  <div class="brand brand--sky" style="left:282px;top:224px">
    <span class="brand__dot" style="width:120px;height:120px"></span>
    <span class="brand__name" style="font-size:44px">Brightlane<br>Detailing</span>
  </div>
  <div class="contact" style="left:232px;top:510px">
    <span class="contact__item">
      <svg width="24" height="24" viewBox="0 0 24 24" aria-hidden="true"><path fill="#fff" d="M6.6 10.8a15.2 15.2 0 0 0 6.6 6.6l2.2-2.2c.3-.3.7-.4 1-.2 1.1.4 2.3.6 3.6.6.6 0 1 .4 1 1V20c0 .6-.4 1-1 1A17 17 0 0 1 3 4c0-.6.4-1 1-1h3.5c.6 0 1 .4 1 1 0 1.3.2 2.5.6 3.6.1.3 0 .7-.2 1z"/></svg>
      0412 555 0 147
    </span>
    <span class="contact__item contact__email">
      <svg width="28" height="20" viewBox="0 0 28 20" aria-hidden="true"><rect x="1.5" y="1.5" width="25" height="17" fill="none" stroke="#fff" stroke-width="2"/><path d="M1.5 1.5 14 11 26.5 1.5M1.5 18.5l9-8M26.5 18.5l-9-8" fill="none" stroke="#fff" stroke-width="2"/></svg>
      HELLO@BRIGHTLANEDETAILING.COM
    </span>
  </div>
</section>
<div class="side-label" style="top:765px">FRNT</div>

<section class="card card--back">
  <div class="service" style="left:70px;top:99px;width:420px">
    <h3 class="service__title">Interior Detail <span class="price">$150</span></h3>
    <ul class="service__list">
      <li>Vacuum and deep clean of carpets, upholstery and leather treatment.</li>
      <li>Interior trim clean and condition.</li>
      <li>Window polish and treatment, steam clean and stain removal.</li>
    </ul>
  </div>
  <div class="service" style="left:70px;top:337px;width:420px">
    <h3 class="service__title">Exterior Detail <span class="price">$250</span></h3>
    <ul class="service__list">
      <li>Extreme wash and polish exterior.</li>
      <li>Trim reviver and protector window.</li>
      <li>Polish and treatment tyre dressing, engine bay cleaned.</li>
    </ul>
  </div>

  <div class="brand brand--sky" style="left:589px;top:74px">
    <span class="brand__dot" style="width:100px;height:100px"></span>
    <span class="brand__name" style="font-size:32px">Brightlane<br>Detailing</span>
  </div>
  <div class="owner">
    <div class="owner__name">DEAN MARLOW</div>
    <div class="owner__role">OWNER/OPERATOR</div>
  </div>

  <div class="service" style="left:548px;top:318px;width:450px">
    <h3 class="service__title" style="margin-left:21px">Full Extreme Detail <span class="price">$350</span></h3>
    <ul class="service__list">
      <li>Extreme wash and polish,<br>tyre dressing, engine bay cleaned.</li>
      <li>Vacuum and deep clean of carpets, upholstery and leather treatment.</li>
      <li>Window polish and treatment.</li>
    </ul>
  </div>
</section>
<div class="side-label" style="top:1515px">BVCK</div>

<section class="banner" style="top:1716px;height:525px">
  <div class="brand brand--white" style="left:306px;top:176px">
    <span class="brand__dot" style="width:176px;height:176px"></span>
    <span class="brand__name" style="font-size:52px">Brightlane<br>Detailing</span>
  </div>
</section>

<div class="brand brand--navy" style="left:306px;top:2416px">
  <span class="brand__dot" style="width:176px;height:176px"></span>
  <span class="brand__name" style="font-size:52px">Brightlane<br>Detailing</span>
</div>

<section class="banner" style="top:2768px;height:529px">
  <div class="brand brand--silver" style="left:306px;top:195px">
    <span class="brand__dot" style="width:176px;height:176px"></span>
    <span class="brand__name" style="font-size:52px">Brightlane<br>Detailing</span>
  </div>
</section>

</body>
</html>
```